Power point presentation optimization, in terms of content design

I have a completed business presentation, with all the texting, but I need some design improvement in terms of text formatting, lettering, text boxes, arrows, bullets, shapes and their formatting, relative location of text boxes and pictures in the slide, etc, etc, so that this specific presentation becomes more visually appealing.
Our company power point template is available.
I´m providing our company power point template (to be used as a reference) as well as the presentation that needs to be improved.

Target Market(s)

Potential partner in business.

Industry/Entity Type

Health

Requirements
Nice to have
• More ellegant collors (more according to the template) on the picture of slide 7. A more elegant dollar image (slide 16).

```html
<!DOCTYPE html>
<html lang="pt">
<head>
<meta charset="utf-8">
<title>Centro Meridiano – Apresentação</title>
<link rel="stylesheet" href="https://fonts.googleapis.com/css2?family=Bebas+Neue&family=Roboto:wght@400;500;700&display=swap">
<style>
:root{
  --page:#d9d9d9;
  --white:#ffffff;
  --teal:#367ea3;
  --navy:#1d3d6e;
  --ink:#231f20;
  --text:#4a4a4a;
  --head:#1d3d6e;
}
*{box-sizing:border-box;margin:0;padding:0}
html,body{width:1200px;height:4046px;overflow:hidden;background:var(--page)}
body{position:relative;font-family:'Roboto',sans-serif;color:var(--text)}
.slide{position:absolute;left:81px;width:1038px;height:584px;background:var(--white);overflow:hidden}
.abs{position:absolute}
.display{font-family:'Bebas Neue',sans-serif;font-weight:400;color:var(--head);letter-spacing:.5px}
/* header */
.header-rule{position:absolute;left:55px;top:2px;width:3px;height:100px;background:var(--navy)}
.brand{position:absolute;left:80px;top:32px;display:flex;align-items:center;gap:10px}
.brand-mark{width:30px;height:30px;background:var(--navy)}
.brand-name{font-family:'Bebas Neue',sans-serif;font-size:28px;color:var(--navy);line-height:1}
.slide-title{position:absolute;right:54px;top:34px;font-size:32px}
/* footer */
.footer{position:absolute;left:55px;top:501px;width:944px;height:48px}
.footer-text{position:absolute;left:0;width:870px;top:16px;text-align:center;font-size:10px;font-weight:700;color:var(--white)}
/* slide 1 */
.cover-brand{position:absolute;left:0;width:100%;top:172px;display:flex;justify-content:center;align-items:center;gap:12px}
.cover-brand .brand-mark{width:46px;height:46px}
.cover-brand .brand-name{font-size:42px}
.cover-title{position:absolute;left:0;width:100%;top:300px;text-align:center;font-size:66px;line-height:1}
.cover-sub{position:absolute;left:0;width:100%;top:388px;text-align:center;font-size:25px;font-weight:500;color:var(--ink)}
/* slide 2 */
.portrait{position:absolute;left:128px;top:124px;width:306px;height:345px;clip-path:polygon(50% 0,100% 25%,100% 75%,50% 100%,0 75%,0 25%);background:radial-gradient(circle at 50% 35%,#5a5552,#1c1a1a 75%)}
.bio{position:absolute;left:520px;width:464px}
.bio-name{position:absolute;right:54px;top:36px;font-size:32px}
.bio h3{font-family:'Bebas Neue',sans-serif;font-weight:400;font-size:22px;line-height:22px;color:var(--head);margin-bottom:12px}
.bio p{font-size:11.5px;line-height:19px;text-align:justify;color:var(--text)}
/* slide 3 */
.sub-head{position:absolute;top:145px;font-size:30px;width:300px;text-align:center}
.tile{position:absolute;top:213px;height:182px;color:var(--white)}
.tile.teal{background:var(--teal)}
.tile.navy{background:var(--navy)}
.tile-frame{position:absolute;inset:13px;border:1.5px solid rgba(255,255,255,.35);display:flex;flex-direction:column;align-items:center;justify-content:center;text-align:center}
.tile-label{font-size:15px;font-weight:700;line-height:19px;margin-top:12px}
.tile-rule{width:26px;height:2px;background:var(--white);margin-top:14px}
/* slide 4 */
.section{background:linear-gradient(180deg,#2a5f93,#275d8f 60%,#2b679a)}
.section-photo{position:absolute;inset:0;background:radial-gradient(ellipse at 50% 55%,rgba(130,165,200,.35),rgba(20,50,90,.15) 70%)}
.section-title{position:absolute;left:0;width:100%;top:195px;text-align:center;font-size:78px;line-height:1;color:var(--white)}
.section-sub{position:absolute;left:0;width:100%;top:312px;text-align:center;font-size:52px;font-weight:700;color:var(--white);letter-spacing:1.5px}
/* slide 5 */
.card{position:absolute;left:0;top:0}
.card-text{position:absolute;left:489px;top:156px;width:461px;font-size:15px;line-height:24.5px;color:var(--text);text-align:justify;text-align-last:right}
.card-text p+p{margin-top:24px}
.feature{position:absolute;font-size:19px;font-weight:700;color:var(--ink);text-align:right;white-space:nowrap}
.feature-dot{position:absolute;width:80px;height:80px;border-radius:50%;display:flex;align-items:center;justify-content:center}
/* slide 6 */
.ticks{position:absolute;left:55px;top:160px;width:480px;list-style:none}
.ticks li{position:relative;padding-left:39px;font-size:18.5px;line-height:38px;color:var(--text)}
.ticks li svg{position:absolute;left:0;top:12px}
.workstation{position:absolute;left:607px;top:133px;width:376px;height:309px;background:linear-gradient(135deg,#1c2838,#35506e 50%,#8a8f96)}
</style>
</head>
<body>

<!-- Slide 1: cover -->
<section class="slide" style="top:110px">
  <svg class="abs" width="1038" height="584" viewBox="0 0 1038 584" aria-hidden="true">
    <polygon points="13,150 64,13 288,118 13,400" fill="var(--teal)"/>
    <polygon points="16,424 136,295 422,573 162,573" fill="var(--ink)"/>
    <polygon points="618,13 720,13 940,180 917,202" fill="var(--navy)"/>
    <polygon points="1030,40 1030,430 877,573 744,471 940,300 905,265 1000,190" fill="var(--navy)"/>
  </svg>
  <div class="cover-brand"><span class="brand-mark"></span><span class="brand-name">Centro Meridiano</span></div>
  <h1 class="cover-title display">Centro Meridiano</h1>
  <p class="cover-sub">Uma perspetiva de 5 minutos</p>
</section>

<!-- Slide 2: biography -->
<section class="slide" style="top:759px">
  <div class="header-rule"></div>
  <div class="brand"><span class="brand-mark"></span><span class="brand-name">Centro Meridiano</span></div>
  <h2 class="bio-name display">Rui Calado</h2>
  <div class="portrait" role="img" aria-label="Retrato do diretor clínico de fato escuro"></div>
  <div class="bio" style="top:94px">
    <h3>Educação Universitária</h3>
    <p>Licenciado em Medicina pela Faculdade de Medicina da Universidade Atlântica (FMA), com a classificação final de 17,17 valores (2000). Doutorado em Medicina pela FMA, aprovado por Unanimidade com Distinção e Louvor (2012).</p>
  </div>
  <div class="bio" style="top:213px">
    <h3>Educação Pós-Graduada</h3>
    <p>Médico Interno de Imagiologia e Radiodiagnóstico do Hospital Universitário de São Brás (2003 a 2008). Visiting Clinical Fellow – Vascular Imaging, Pacific Coast University (2008). Visiting Clinical Fellow – Musculoskeletal Imaging, Service de Radiologie Ostéoarticulaire, Hôpital Saint-Lumière, Paris (2008).</p>
  </div>
  <div class="bio" style="top:370px">
    <h3>Funções Actuais</h3>
    <p>CEO, Centro Meridiano (desde 2013). Membro da Comissão Editorial do “Global Journal of Musculoskeletal Care” (desde 2014). Grau de Consultor (Imagiologia) pelo Colégio Nacional de Imagiologia (desde 2018). Professor Auxiliar Convidado e Regente de Disciplina da Escola Médica Horizonte (desde 2018). Investigador do Integrated Health Research Unit, IHRU/EMH (desde 2018).</p>
  </div>
  <div class="footer">
    <svg class="abs" width="944" height="48" aria-hidden="true"><polygon points="0,0 870,0 846,48 0,48" fill="var(--teal)"/><polygon points="882,0 944,0 920,48 858,48" fill="var(--navy)"/></svg>
    <p class="footer-text">© 2022 Meridiano. Alle Rechte vorbehalten</p>
  </div>
</section>

<!-- Slide 3: challenge -->
<section class="slide" style="top:1407px">
  <div class="header-rule"></div>
  <div class="brand"><span class="brand-mark"></span><span class="brand-name">Centro Meridiano</span></div>
  <h2 class="slide-title display">Imagiologia em Angola</h2>
  <h3 class="sub-head display" style="left:136px">A Dificuldade</h3>
  <h3 class="sub-head display" style="left:601px">A Hipótese</h3>

  <div class="tile teal" style="left:71px;width:210px"><div class="tile-frame">
    <svg width="44" height="44" viewBox="0 0 44 44" aria-hidden="true"><circle cx="22" cy="22" r="19" fill="none" stroke="#fff" stroke-width="3"/><circle cx="22" cy="22" r="4" fill="#fff"/><path d="M22 22 L14 10 A14 14 0 0 1 30 10 Z M22 22 L36 24 A14 14 0 0 1 28 35 Z M22 22 L16 35 A14 14 0 0 1 8 24 Z" fill="#fff"/></svg>
    <p class="tile-label">Falta de Médicos<br>Radiologistas</p><span class="tile-rule"></span></div></div>

  <div class="tile navy" style="left:293px;width:209px"><div class="tile-frame">
    <svg width="30" height="46" viewBox="0 0 30 46" aria-hidden="true"><rect x="12" y="0" width="6" height="8" fill="#fff"/><rect x="6" y="8" width="18" height="26" rx="2" fill="#fff"/><rect x="10" y="14" width="10" height="2" fill="var(--navy)"/><rect x="10" y="20" width="10" height="2" fill="var(--navy)"/><rect x="10" y="26" width="10" height="2" fill="var(--navy)"/><rect x="14" y="34" width="2" height="12" fill="#fff"/></svg>
    <p class="tile-label">Falta de Médicos<br>Radiologistas</p><span class="tile-rule"></span></div></div>

  <div class="tile teal" style="left:538px;width:210px"><div class="tile-frame">
    <svg width="44" height="40" viewBox="0 0 44 40" aria-hidden="true"><rect x="2" y="2" width="30" height="34" fill="none" stroke="#fff" stroke-width="2.5"/><rect x="7" y="9" width="8" height="8" fill="#fff"/><rect x="18" y="10" width="9" height="2" fill="#fff"/><rect x="18" y="15" width="9" height="2" fill="#fff"/><rect x="7" y="23" width="14" height="2" fill="#fff"/><circle cx="33" cy="29" r="8" fill="var(--teal)" stroke="#fff" stroke-width="2.5"/><path d="M29 29 l3 3 l5 -6" fill="none" stroke="#fff" stroke-width="2"/></svg>
    <p class="tile-label">Expatriar Profissionais<br>Portugueses</p><span class="tile-rule"></span></div></div>

  <div class="tile navy" style="left:759px;width:208px"><div class="tile-frame">
    <svg width="40" height="40" viewBox="0 0 40 40" aria-hidden="true"><circle cx="20" cy="16" r="12" fill="none" stroke="#fff" stroke-width="3"/><rect x="14" y="12" width="12" height="8" fill="#fff"/><rect x="4" y="30" width="32" height="4" fill="#fff"/><path d="M12 26 l-4 4 M28 26 l4 4" stroke="#fff" stroke-width="3"/></svg>
    <p class="tile-label">Elevado custo</p><span class="tile-rule"></span></div></div>

  <div class="footer">
    <svg class="abs" width="944" height="48" aria-hidden="true"><polygon points="0,0 870,0 846,48 0,48" fill="var(--teal)"/><polygon points="882,0 944,0 920,48 858,48" fill="var(--navy)"/></svg>
    <p class="footer-text">© 2022 Meridiano. Alle Rechte vorbehalten</p>
  </div>
</section>

<!-- Slide 4: section divider -->
<section class="slide section" style="top:2055px">
  <div class="section-photo" role="img" aria-label="Médico com exames de imagiologia sobrepostos em tom azul"></div>
  <h2 class="section-title display">Imagiologia em Angola</h2>
  <p class="section-sub">A SOLUÇÃO - TELERADIOLOGIA</p>
</section>

<!-- Slide 5: about -->
<section class="slide" style="top:2703px">
  <div class="header-rule"></div>
  <div class="brand"><span class="brand-mark"></span><span class="brand-name">Centro Meridiano</span></div>
  <h2 class="slide-title display">Sobre Nós</h2>
  <svg class="card" width="1038" height="584" viewBox="0 0 1038 584" aria-hidden="true">
    <defs><filter id="card-shadow" x="-5%" y="-5%" width="110%" height="110%"><feDropShadow dx="0" dy="1" stdDeviation="3" flood-color="#000" flood-opacity=".25"/></filter></defs>
    <polygon points="343,109 985,109 985,470 461,470" fill="#fff" filter="url(#card-shadow)"/>
  </svg>
  <div class="card-text">
    <p>O Centro Internacional Meridiano Professor Doutor Rui Calado nasceu da necessidade de assegurar uma resposta de teleradiologia de elevada qualidade, suportada por um corpo clínico de topo.</p>
    <p>Os nossos médicos são sub-especializados nas diferentes áreas: sistema musculo-esquelético, medicina desportiva, neurorradiologia, abdómen, pélvis, sistema cardiovascular e mama. Todos os nossos exames recebem assim uma consultadoria diferenciada por especialistas de renome, assegurando o máximo rigor diagnóstico.</p>
  </div>

  <p class="feature" style="right:747px;top:171px">Os melhores Médicos</p>
  <div class="feature-dot" style="left:323px;top:144px;background:var(--teal)">
    <svg width="34" height="38" viewBox="0 0 34 38" aria-hidden="true"><path d="M17 2 L31 7 V18 C31 27 24 33 17 36 C10 33 3 27 3 18 V7 Z" fill="none" stroke="#fff" stroke-width="3"/><path d="M17 11 v14 M10 18 h14" stroke="#fff" stroke-width="4"/></svg>
  </div>

  <p class="feature" style="right:719px;top:279px">EM LUANDA</p>
  <div class="feature-dot" style="left:353px;top:252px;background:var(--navy)">
    <svg width="36" height="32" viewBox="0 0 36 32" aria-hidden="true"><path d="M2 6 H14 L17 10 H34 V30 H2 Z" fill="#fff"/><path d="M18 14 v12 M12 20 h12" stroke="var(--navy)" stroke-width="3.5"/></svg>
  </div>

  <p class="feature" style="right:691px;top:387px">Baixo custo</p>
  <div class="feature-dot" style="left:379px;top:360px;background:var(--ink)">
    <svg width="36" height="30" viewBox="0 0 36 30" aria-hidden="true"><rect x="12" y="2" width="12" height="6" fill="none" stroke="#fff" stroke-width="2.5"/><rect x="2" y="7" width="32" height="21" rx="3" fill="#fff"/><circle cx="18" cy="17.5" r="7" fill="var(--ink)"/><path d="M18 13 v9 M13.5 17.5 h9" stroke="#fff" stroke-width="2.5"/></svg>
  </div>

  <div class="footer">
    <svg class="abs" width="944" height="48" aria-hidden="true"><polygon points="0,0 870,0 846,48 0,48" fill="var(--teal)"/><polygon points="882,0 944,0 920,48 858,48" fill="var(--navy)"/></svg>
    <p class="footer-text">© 2022 Meridiano. Alle Rechte vorbehalten</p>
  </div>
</section>

<!-- Slide 6: costs -->
<section class="slide" style="top:3351px">
  <div class="header-rule"></div>
  <div class="brand"><span class="brand-mark"></span><span class="brand-name">Centro Meridiano</span></div>
  <h2 class="slide-title display">Custos Controlados</h2>
  <ul class="ticks">
    <li><svg width="16" height="16" viewBox="0 0 16 16" aria-hidden="true"><circle cx="8" cy="8" r="8" fill="var(--navy)"/><path d="M4.5 8.2 l2.3 2.3 l4.7 -4.8" fill="none" stroke="#fff" stroke-width="2"/></svg>Despesa com a montagem da plataforma informática fica completamente do nosso lado</li>
    <li><svg width="16" height="16" viewBox="0 0 16 16" aria-hidden="true"><circle cx="8" cy="8" r="8" fill="var(--navy)"/><path d="M4.5 8.2 l2.3 2.3 l4.7 -4.8" fill="none" stroke="#fff" stroke-width="2"/></svg>Não existe qualquer pagamento inicial</li>
    <li><svg width="16" height="16" viewBox="0 0 16 16" aria-hidden="true"><circle cx="8" cy="8" r="8" fill="var(--navy)"/><path d="M4.5 8.2 l2.3 2.3 l4.7 -4.8" fill="none" stroke="#fff" stroke-width="2"/></svg>Não existem quaisquer custos fixos ou um mínimo de exames obrigatório</li>
    <li><svg width="16" height="16" viewBox="0 0 16 16" aria-hidden="true"><circle cx="8" cy="8" r="8" fill="var(--navy)"/><path d="M4.5 8.2 l2.3 2.3 l4.7 -4.8" fill="none" stroke="#fff" stroke-width="2"/></svg>Temos simplesmente um preço por relatório</li>
    <li><svg width="16" height="16" viewBox="0 0 16 16" aria-hidden="true"><circle cx="8" cy="8" r="8" fill="var(--navy)"/><path d="M4.5 8.2 l2.3 2.3 l4.7 -4.8" fill="none" stroke="#fff" stroke-width="2"/></svg>São faturados apenas os relatórios efectivados</li>
  </ul>
  <div class="workstation" role="img" aria-label="Radiologista a analisar exames em monitores de diagnóstico"></div>
  <div class="footer">
    <svg class="abs" width="944" height="48" aria-hidden="true"><polygon points="0,0 870,0 846,48 0,48" fill="var(--teal)"/><polygon points="882,0 944,0 920,48 858,48" fill="var(--navy)"/></svg>
    <p class="footer-text">© 2022 Meridiano. Alle Rechte vorbehalten</p>
  </div>
</section>

</body>
</html>
```